Velisto Events Business Card

We need a business cards that stands out to our clients. We are company who targets prestige clients to spend money with us on experiences, so our image needs to be prestige
Target Market(s)
Corporate
Contact Information for Business Card
There will be four different names on the business cards
Dana Morrowby
Director
O: 02 5147 3086
M: 0451 692 038
E: info@velistoevents.example.au
Facebook: @velistoevents
Instagram: velistoevents
www.velistoevents.example.au
Nathaniel Morrowby
Director
O: 02 5147 3086
M: 0467 215 904
Facebook: @velistoevents
Instagram: velistoevents
www.velistoevents.example.au
Teodor Vinkel
Director
O: 02 5147 3086
M: 0478 903 527
Facebook: @velistoevents
Instagram: velistoevents
www.velistoevents.example.au
Mabel Hartung
Director
O: 02 5147 3086
Facebook: @velistoevents
Instagram: velistoevents
www.velistoevents.example.au
Colors
Designer to choose colors to be used in the design.
Look and feel

```html
<!DOCTYPE html>
<html lang="en">
<head>
<meta charset="utf-8">
<title>Velisto Events — Business Card</title>
<link href="https://fonts.googleapis.com/css2?family=Cinzel:wght@400;700&family=Merriweather+Sans:wght@300;400&display=swap" rel="stylesheet">
<style>
  :root {
    --backdrop: #1c1c1e;
    --card: #252152;
    --card-edge: #2c2860;
    --gold: #c9a45c;
    --gold-soft: #b8935a;
    --ink-light: #e4e1ef;
    --ink-muted: #c9c5dc;
    --dot: #8e86c4;
  }
  * { margin: 0; padding: 0; box-sizing: border-box; }
  html, body {
    width: 1200px;
    height: 852px;
    overflow: hidden;
    background: var(--backdrop);
  }
  .sheet {
    width: 1200px;
    height: 852px;
    display: flex;
    flex-direction: column;
    align-items: center;
    justify-content: center;
    gap: 44px;
  }
  .card {
    position: relative;
    width: 560px;
    height: 340px;
    border-radius: 22px;
    background: linear-gradient(135deg, var(--card-edge), var(--card));
    box-shadow: 0 10px 30px rgba(0,0,0,.45);
    overflow: hidden;
  }
  .wordmark {
    font-family: "Cinzel", serif;
    font-weight: 400;
    color: var(--gold);
    text-align: center;
    line-height: 1;
  }
  .wordmark__name { display: block; letter-spacing: .32em; }
  .wordmark__sub { display: block; letter-spacing: .5em; margin-top: 8px; }

  /* Front */
  .card--front .wordmark {
    position: absolute;
    left: 0; right: 0;
    top: 118px;
  }
  .card--front .wordmark__name { font-size: 34px; }
  .card--front .wordmark__sub { font-size: 13px; }
  .socials {
    position: absolute;
    left: 0; right: 0;
    bottom: 40px;
    display: flex;
    justify-content: center;
    gap: 26px;
    font-family: "Merriweather Sans", sans-serif;
    font-weight: 300;
    font-size: 13px;
    color: var(--ink-light);
  }
  .socials__item { display: flex; align-items: center; gap: 7px; }
  .socials__dot {
    width: 14px; height: 14px;
    border-radius: 50%;
    background: var(--dot);
  }

  /* Back */
  .card--back .wordmark {
    position: absolute;
    left: 48px;
    top: 142px;
    text-align: left;
  }
  .card--back .wordmark__name { font-size: 25px; }
  .card--back .wordmark__sub { font-size: 10px; padding-left: 42px; }
  .contact {
    position: absolute;
    left: 330px;
    top: 122px;
    font-family: "Merriweather Sans", sans-serif;
    color: var(--ink-light);
  }
  .contact__name {
    font-family: "Cinzel", serif;
    font-weight: 700;
    font-size: 17px;
    letter-spacing: .06em;
    color: var(--gold);
  }
  .contact__role {
    font-size: 12px;
    font-weight: 300;
    color: var(--ink-muted);
    margin-top: 4px;
    margin-bottom: 14px;
  }
  .contact__list { list-style: none; }
  .contact__line {
    display: flex;
    align-items: center;
    gap: 9px;
    font-size: 12.5px;
    font-weight: 300;
    margin-bottom: 7px;
  }
  .contact__icon { width: 13px; height: 13px; flex: none; }
</style>
</head>
<body>
<main class="sheet">

  <section class="card card--front" aria-label="Card front">
    <div class="wordmark">
      <span class="wordmark__name">VELISTO</span>
      <span class="wordmark__sub">EVENTS</span>
    </div>
    <div class="socials">
      <span class="socials__item"><span class="socials__dot"></span>@velistoevents</span>
      <span class="socials__item"><span class="socials__dot"></span>velistoevents</span>
    </div>
  </section>

  <section class="card card--back" aria-label="Card back">
    <div class="wordmark">
      <span class="wordmark__name">VELISTO</span>
      <span class="wordmark__sub">EVENTS</span>
    </div>
    <div class="contact">
      <p class="contact__name">DANA MORROWBY</p>
      <p class="contact__role">Director</p>
      <ul class="contact__list">
        <li class="contact__line">
          <svg class="contact__icon" viewBox="0 0 16 16" aria-hidden="true">
            <rect x="4" y="1" width="8" height="14" rx="1.5" fill="none" stroke="#c9a45c" stroke-width="1.6"/>
            <circle cx="8" cy="12.3" r="0.9" fill="#c9a45c"/>
          </svg>
          0451 692 038
        </li>
        <li class="contact__line">
          <svg class="contact__icon" viewBox="0 0 16 16" aria-hidden="true">
            <rect x="1" y="3" width="14" height="10" rx="1" fill="none" stroke="#c9a45c" stroke-width="1.6"/>
            <path d="M1.5 3.5 L8 9 L14.5 3.5" fill="none" stroke="#c9a45c" stroke-width="1.6"/>
          </svg>
          info@velistoevents.example.au
        </li>
        <li class="contact__line">
          <svg class="contact__icon" viewBox="0 0 16 16" aria-hidden="true">
            <circle cx="8" cy="8" r="6.5" fill="none" stroke="#c9a45c" stroke-width="1.5"/>
            <ellipse cx="8" cy="8" rx="2.8" ry="6.5" fill="none" stroke="#c9a45c" stroke-width="1.2"/>
            <path d="M1.5 8 H14.5" stroke="#c9a45c" stroke-width="1.2"/>
          </svg>
          www.velistoevents.example.au
        </li>
      </ul>
    </div>
  </section>

</main>
</body>
</html>
```